Business Card Design

RETAIL HIGH END CONTEMPORARY WOMEN'S CLOTHING STORE
MODERN, SIMPLE, CLEAN, COOL

WE ARE ALL ABOUT NY and CALIF STYLE.... CLASSY but EDGY..
COOLEST DENIM , Trendsetting, NEUTRAL Pallettes,
Collections : Fig and Stone, Dorian Vesk, PMW, K47, QTB
Don't need names of collections on card. thats just good info
for designer of card.

WOULD LIKE THE FONT TO BE INTERESTING, but CLEAN
We are on facebook daily with photos of outfits we put together
which you can look up and friend us.... MolvaHarbor
Also on instagram .
Open to options on color and size, but need cool and fresh.

Contact Information for Business Card

DELLA 5417 Larkmoor Rd. #309 Ember Court Arcade..Va. Beach, Va. 23987
Phone 757.386.5049 Fax 757.386-2613 EMAIL..DELLAMODE@QUILLBOX.COM

```html
<!DOCTYPE html>
<html lang="en">
<head>
<meta charset="utf-8">
<title>DELLA — Business Card</title>
<link rel="stylesheet" href="https://fonts.googleapis.com/css2?family=Tulpen+One&display=swap">
<style>
  :root {
    --card-blue: #55c8ea;
    --ink-white: #ffffff;
  }
  html, body {
    margin: 0;
    padding: 0;
    overflow: hidden;
    background: var(--card-blue);
  }
  .business-card {
    position: relative;
    width: 1200px;
    height: 703px;
    background: var(--card-blue);
    overflow: hidden;
    font-family: "Tulpen One", "Arial Narrow", sans-serif;
    color: var(--ink-white);
  }
  .brand-name {
    position: absolute;
    left: 0;
    top: 0;
    width: 400px;
    height: 703px;
  }
  .brand-name text {
    font-family: "Tulpen One", "Arial Narrow", sans-serif;
    fill: var(--ink-white);
  }
  .contact-line {
    position: absolute;
    right: 50px;
    margin: 0;
    line-height: 1;
    white-space: nowrap;
    text-transform: uppercase;
    font-weight: 400;
    letter-spacing: 0.02em;
  }
  .street    { top: 44px;  font-size: 98px; }
  .suite     { top: 138px; font-size: 78px; }
  .city      { top: 218px; font-size: 78px; }
  .phone     { top: 414px; font-size: 108px; }
  .fax       { top: 516px; font-size: 80px; }
  .email     { top: 586px; font-size: 80px; }
</style>
</head>
<body>
  <main class="business-card">
    <svg class="brand-name" viewBox="0 0 400 703" aria-label="DELLA">
      <text transform="translate(325,655) rotate(-90)" x="0" y="0"
            font-size="390" textLength="605" lengthAdjust="spacingAndGlyphs">DELLA</text>
    </svg>

    <address class="contact-block" style="font-style: normal;">
      <p class="contact-line street">5417 Larkmoor Rd</p>
      <p class="contact-line suite">#309 Ember Court Arcade</p>
      <p class="contact-line city">Virginia Beach, VA 23987</p>
      <p class="contact-line phone">757.386.5049</p>
      <p class="contact-line fax">757.386.2613</p>
      <p class="contact-line email">dellamode@quillbox.com</p>
    </address>
  </main>
</body>
</html>
```